Dynamic Business Card for Sports Supplements Company

Hi! I'm looking for an awesome business card to match my existing sports supplement company. I have uploaded my current company logo and screenshot of the front page of my website.

I would like to have something dynamic and interesting and utilize the colors in the website - the reds and purples

The business card should be double sided and focus on a unique eye-catching design on the back and include all the relevant company info.

Most importantly, it should say somewhere: "Sign up on our website for a coupon code."

Target Market(s)

Mostly for women gym goers but it shouldn't be too feminine. It should be in keeping with the website design. It should flow and clearly be connected to it

Industry/Entity Type

Business

Contact Information for Business Card

Lorena K. Vasquez
CEO
LVasquez@Fortivanco.example
www.fortivanco.example
614.275.3081
P.O. Box 48317
Halden, Oregon 22417

Sign up on our website for a coupon code

Font styles to use
Serif
Sans Serif
Other font styles liked:
• Novecento font family and "Fortivan" is in AR Destine font

Requirements
Must have
• One side should be a bold Fortivan logo design. Even just the symbol itself may be o.k. (see attached file)

```html
<!DOCTYPE html>
<html lang="en">
<head>
<meta charset="utf-8">
<title>Fortivan Business Card</title>
<link href="https://fonts.googleapis.com/css2?family=Arimo:wght@400;700&display=swap" rel="stylesheet">
<style>
  :root {
    --backdrop: #3a3431;
    --card: #141414;
    --card-edge: #1c1c1c;
    --text: #f2f2f2;
    --text-muted: #9a9a9a;
    --gloss: #5a5a5a;
    --accent: #e5242f;
    --divider: #4a4a4a;
  }
  * { box-sizing: border-box; margin: 0; padding: 0; }
  html, body {
    width: 1200px; height: 864px; overflow: hidden;
    background: var(--backdrop);
    font-family: "Arimo", Arial, sans-serif;
  }
  .sheet {
    width: 1200px; height: 864px;
    display: flex; align-items: center; justify-content: center; gap: 44px;
  }
  .card {
    width: 520px; height: 297px;
    background: linear-gradient(135deg, var(--card-edge), var(--card));
    border-radius: 3px;
    box-shadow: 0 10px 30px rgba(0,0,0,.45);
    position: relative; overflow: hidden;
  }
  /* front */
  .card-front {
    display: flex; flex-direction: column; justify-content: center; padding-left: 70px;
  }
  .brand-front {
    display: flex; align-items: center; gap: 12px;
    color: var(--gloss); font-weight: 700; font-size: 40px; letter-spacing: 1px;
  }
  .brand-front .mark { width: 30px; height: 30px; background: var(--gloss); }
  .coupon {
    margin-top: 22px; color: var(--text-muted); font-size: 14px;
  }
  /* back */
  .card-back { display: flex; align-items: center; }
  .brand-back {
    width: 230px; display: flex; align-items: center; justify-content: center; gap: 10px;
    color: var(--text); font-weight: 700; font-size: 34px;
  }
  .brand-back .mark { width: 26px; height: 26px; background: var(--accent); }
  .divider { width: 1px; height: 120px; background: var(--divider); }
  .contact { padding-left: 22px; color: var(--text); font-size: 14px; line-height: 1.35; }
  .contact-name { color: var(--accent); font-size: 19px; line-height: 1.1; }
  .contact-title { margin-bottom: 14px; }
  .contact-address { margin-bottom: 6px; }
  .contact-line { display: flex; align-items: center; gap: 8px; }
  .contact-line svg { width: 12px; height: 12px; flex: none; }
</style>
</head>
<body>
<main class="sheet">
  <section class="card card-front" aria-label="Card front">
    <div class="brand-front"><span class="mark"></span>FORTIVAN</div>
    <p class="coupon">Sign up on our website for a coupon code</p>
  </section>

  <section class="card card-back" aria-label="Card back">
    <div class="brand-back"><span class="mark"></span>Fortivan</div>
    <div class="divider"></div>
    <div class="contact">
      <p class="contact-name">Lorena K. Vasquez</p>
      <p class="contact-title">CEO</p>
      <p class="contact-address">P.O. Box 48317<br>Halden, Oregon 22417</p>
      <p class="contact-line">
        <svg viewBox="0 0 12 12" aria-hidden="true"><path fill="var(--accent)" d="M2 1h2l1 3-1.3 1a6 6 0 0 0 3.3 3.3L8 7l3 1v2a1 1 0 0 1-1 1A9 9 0 0 1 1 2a1 1 0 0 1 1-1z"/></svg>
        614.275.3081
      </p>
      <p class="contact-line">
        <svg viewBox="0 0 12 12" aria-hidden="true"><rect x="0.5" y="2" width="11" height="8" rx="1" fill="var(--accent)"/><path d="M1 3l5 4 5-4" stroke="var(--card)" fill="none"/></svg>
        LVasquez@Fortivanco.example
      </p>
      <p class="contact-line">
        <svg viewBox="0 0 12 12" aria-hidden="true"><circle cx="6" cy="6" r="5.5" fill="var(--accent)"/><path d="M0.5 6h11M6 0.5c-2.5 3-2.5 8 0 11M6 0.5c2.5 3 2.5 8 0 11" stroke="var(--card)" stroke-width="0.8" fill="none"/></svg>
        www.fortivanco.example
      </p>
    </div>
  </section>
</main>
</body>
</html>
```